Startup company business card (Media & Advertising)

we need a business card design for a company that is a startup in the media and aggregation industry. Card needs to look funky and of a new breed/modern and upmarket.

Target Market(s)

advertisers/ brand agencies & media publishers

Industry/Entity Type

Advertising

Contact Information for Business Card

Please ensure the front face signifies our brand (plumvexo.com) and back has details for the contact. Standard contact such as phone , address, email , website etc.

Font styles to use
Other font styles liked:
• use styleguide and logo font and color

Colors

Designer to choose colors to be used in the design.

Requirements
Must have
• We are disrupting the media and agency industry so subtlety would be good to use imagery to signify this
Nice to have
• Please use logo colors for branding
Should not have
• be as creative and provide few options. Pick a brand color from logo and styleguide

```html
<!DOCTYPE html>
<html lang="en">
<head>
<meta charset="UTF-8">
<title>Plumvexo Business Card</title>
<link rel="stylesheet" href="https://fonts.googleapis.com/css2?family=Zilla+Slab:wght@700&family=Montserrat:wght@400;600;700;800&display=swap">
<style>
  :root {
    --canvas: #07090b;
    --brand-red: #a8141c;
    --accent-red: #e8333c;
    --soft-red: #f05a62;
    --ink: #111111;
    --paper: #ffffff;
    --muted: #8a8a8a;
    --rule: #9a9a9a;
  }
  html, body {
    margin: 0;
    padding: 0;
    width: 927px;
    height: 1200px;
    overflow: hidden;
    background: var(--canvas);
  }
  .canvas {
    position: relative;
    width: 927px;
    height: 1200px;
  }
  .card {
    position: absolute;
    overflow: hidden;
  }
  .card--front {
    left: 286px; top: 357px;
    width: 359px; height: 235px;
    background: var(--brand-red);
  }
  .card--back {
    left: 283px; top: 654px;
    width: 361px; height: 237px;
    background: var(--paper);
  }
  .brand {
    position: absolute;
    display: flex;
    align-items: center;
  }
  .brand__dot {
    border-radius: 50%;
    flex: none;
  }
  .brand__name {
    font-family: "Zilla Slab", Georgia, serif;
    font-weight: 700;
    line-height: 1;
  }
  .card--front .brand { left: 50px; top: 94px; gap: 22px; }
  .card--front .brand__dot { width: 52px; height: 52px; background: var(--soft-red); }
  .card--front .brand__name { font-size: 46px; color: var(--paper); }

  .card--back .brand { left: 88px; top: 34px; gap: 14px; }
  .card--back .brand__dot { width: 40px; height: 40px; background: var(--accent-red); }
  .card--back .brand__name { font-size: 34px; color: var(--ink); }

  .tab {
    position: absolute;
    bottom: 0;
    height: 18px;
    border-radius: 6px 6px 0 0;
    text-align: center;
    font-family: "Montserrat", Arial, sans-serif;
    box-sizing: border-box;
  }
  .tab--web {
    left: 88px; width: 183px;
    background: var(--paper);
    border: 1.5px solid var(--ink);
    border-bottom: none;
    color: var(--ink);
    font-size: 15px;
    font-weight: 600;
    line-height: 18px;
  }
  .tab--tagline {
    left: 90px; width: 182px;
    background: var(--accent-red);
    color: var(--paper);
    font-size: 10.5px;
    font-weight: 400;
    line-height: 18px;
  }
  .person {
    position: absolute;
    left: 35px; top: 117px;
    font-family: "Montserrat", Arial, sans-serif;
  }
  .person__name {
    font-size: 19px;
    letter-spacing: 0.3px;
    color: var(--accent-red);
    line-height: 1;
  }
  .person__name strong { font-weight: 800; }
  .person__name span { font-weight: 400; }
  .person__role {
    font-size: 9px;
    color: var(--muted);
    margin-top: 1px;
  }
  .divider {
    position: absolute;
    left: 176px; top: 103px;
    width: 1px; height: 55px;
    background: var(--rule);
  }
  .contact {
    position: absolute;
    left: 186px; top: 109px;
    margin: 0; padding: 0;
    list-style: none;
    font-family: "Montserrat", Arial, sans-serif;
    font-size: 8.5px;
    font-weight: 700;
    color: var(--ink);
  }
  .contact li {
    display: flex;
    align-items: center;
    gap: 8px;
    height: 16.5px;
  }
  .contact svg { width: 9px; height: 9px; flex: none; fill: var(--accent-red); }
</style>
</head>
<body>
<main class="canvas">
  <section class="card card--front" aria-label="Card front">
    <div class="brand">
      <span class="brand__dot"></span>
      <span class="brand__name">plumvexo</span>
    </div>
    <div class="tab tab--web">plumvexo.com</div>
  </section>

  <section class="card card--back" aria-label="Card back">
    <div class="brand">
      <span class="brand__dot"></span>
      <span class="brand__name">plumvexo</span>
    </div>
    <div class="person">
      <div class="person__name"><strong>DARA</strong> <span>QUILL</span></div>
      <div class="person__role">Founder</div>
    </div>
    <div class="divider"></div>
    <ul class="contact">
      <li>
        <svg viewBox="0 0 10 10"><path d="M5 0a3.5 3.5 0 0 0-3.5 3.5C1.5 6 5 10 5 10s3.5-4 3.5-6.5A3.5 3.5 0 0 0 5 0zm0 5a1.4 1.4 0 1 1 0-2.8A1.4 1.4 0 0 1 5 5z"/></svg>
        123 Dummy, Lorem Ipsum
      </li>
      <li>
        <svg viewBox="0 0 10 10"><path d="M2 0.5l1.8 2-1 1.2c.6 1.3 1.6 2.3 2.9 2.9l1.2-1 2 1.8-1 2C4.5 9.2.8 5.5.5 1.5z"/></svg>
        +00 1234 5XXX 9012
      </li>
      <li>
        <svg viewBox="0 0 10 10"><rect x="0.5" y="2" width="9" height="6.5" rx="0.8"/></svg>
        info@email space
      </li>
    </ul>
    <div class="tab tab--tagline">Advertise anywhere, anytime!</div>
  </section>
</main>
</body>
</html>
```